business card design - photography

I am a fine art photographer. I would like to approach galleries to exhibit my work and need a business card.

The card should convey creativity and simplicity.
I would like a double sided card.

Some options:
1. An all white card with raised or embossed text or design to create a tactile finish.
2. a white and dark grey design would also work well.
3. Would be great to use my name as part of the design but not essential.
4. My name and title on the front, other details on the back of card.

The final design should be simple, minimal, elegant and innovative.
Being minimal, it will be more about texture, text size and placement.

examples of designs I would prefer provided here:
http://plimvarka.com/ideas/40-quiet-and-refined-card-layouts

I'm also open to other designs that may be unusual and unique.

Love this:
http://www.snapvelo.com/pics/morningverselog/583014927
Updates

I have uploaded a psd file after playing around in photoshop with various fonts.  I like the font (which I downloaded from glyphmorra.com called Arual) but the design probably needs some refining.  I hope this helps.  If you'd like me to change the format of the file, please let me know.

Ilvane

Target Market(s)

Art Gallery owners/administrators and customers.

Industry/Entity Type

Business

Requirements
Must have
• A unique look.

Matte, silky finish or heavy textured stock. Double-sided card.

Front:
my name
photography by

Back:
phone no
email
web address
Nice to have
• Letterpress
embrossed
Clean fonts
Should not have
• Do not use illustrations of cameras or lenses.
No frames around the card edge.

```html
<!DOCTYPE html>
<html lang="en">
<head>
<meta charset="utf-8">
<title>Ilvane Corvell Photography – Business Card</title>
<link rel="stylesheet" href="https://fonts.googleapis.com/css2?family=Roboto+Slab:wght@800&family=Josefin+Sans:wght@300&family=Jost:wght@400&display=swap">
<style>
  :root {
    --band: #1d2020;
    --paper: #ffffff;
    --ink: #1b1b1b;
    --name: #ffffff;
  }
  * { margin: 0; padding: 0; box-sizing: border-box; }
  html, body {
    width: 1200px;
    height: 1033px;
    overflow: hidden;
    background: var(--paper);
  }
  .card {
    position: relative;
    width: 1200px;
    height: 1033px;
    background: var(--paper);
  }
  .card__front {
    position: absolute;
    left: 0; top: 0;
    width: 1200px;
    height: 516px;
    background: var(--band);
  }
  .brand {
    position: absolute;
    right: 194px;
    top: 196px;
    text-align: right;
    color: var(--name);
  }
  .brand__name {
    font-family: "Roboto Slab", serif;
    font-weight: 800;
    font-size: 124px;
    line-height: 1;
    letter-spacing: -4px;
  }
  .brand__title {
    font-family: "Josefin Sans", sans-serif;
    font-weight: 300;
    font-size: 29px;
    letter-spacing: 23px;
    margin-right: -23px;
    margin-top: 4px;
    line-height: 1;
  }
  .contacts {
    position: absolute;
    left: 337px;
    top: 655px;
    list-style: none;
    color: var(--ink);
    font-family: "Jost", sans-serif;
    font-weight: 400;
    font-size: 51px;
    letter-spacing: -1px;
  }
  .contacts__item {
    display: flex;
    align-items: center;
    height: 96px;
  }
  .contacts__icon {
    width: 52px;
    height: 52px;
    margin-right: 26px;
    flex: none;
  }
</style>
</head>
<body>
  <main class="card">
    <section class="card__front">
      <div class="brand">
        <div class="brand__name">Ilvane Corvell</div>
        <div class="brand__title">PHOTOGRAPHY</div>
      </div>
    </section>

    <ul class="contacts">
      <li class="contacts__item">
        <svg class="contacts__icon" viewBox="0 0 52 52" aria-hidden="true">
          <path d="M3 18c0-6 10-9 23-9s23 3 23 9v4h-11v-5c-4-1-8-1-12-1s-8 0-12 1v5H3z" fill="var(--ink)"/>
          <path d="M10 24h32l5 10v12H5V34z" fill="var(--ink)"/>
          <circle cx="26" cy="34" r="6" fill="var(--paper)"/>
        </svg>
        <span>0418 270 394</span>
      </li>
      <li class="contacts__item">
        <svg class="contacts__icon" viewBox="0 0 52 52" aria-hidden="true">
          <rect x="1" y="12" width="50" height="30" fill="var(--ink)"/>
          <path d="M3 14l23 17 23-17" fill="none" stroke="var(--paper)" stroke-width="2.5"/>
          <path d="M3 40l17-14M49 40L32 26" fill="none" stroke="var(--paper)" stroke-width="2"/>
        </svg>
        <span>icorvell@mailbay.com</span>
      </li>
      <li class="contacts__item">
        <svg class="contacts__icon" viewBox="0 0 52 52" aria-hidden="true">
          <g fill="none" stroke="var(--ink)" stroke-width="2.6">
            <circle cx="26" cy="26" r="22"/>
            <ellipse cx="26" cy="26" rx="10" ry="22"/>
            <line x1="26" y1="4" x2="26" y2="48"/>
            <line x1="4" y1="26" x2="48" y2="26"/>
            <path d="M8 14h36M8 38h36"/>
          </g>
        </svg>
        <span>www.ilvanecorvell.com</span>
      </li>
    </ul>
  </main>
</body>
</html>
```